Mobile Optometry needs descriptive brochure and business cards for patients

I need a brochure design and business cards for a new optometry service that brings full ocular examination, refraction, and spectacle dispensing to the patient in need.
I will mainly be working out of senior homes so it needs to be very legible NO SMALL PRINT, CLEAR, CONSCIENCE.
The final design needs to incorporate the logo and colouring that was just selected from a previous project. I will add this file as soon as I get the final changes back from the designer.

Here is what I would like in the broacher. I don't have a fax number, website address, email address set up yet but have room for this.

Note: I have attached the logo I selected for the company. I may not have attached the most detailed version but this will give you an idea of colouring and style. I will upload the proper image soon.

Routine eye examinations are crucial for early detection of diseases of the eye and effects of systemic conditions for everybody. As we age we are at higher risk of vision loss due to Glaucoma, Age-related Macular Degeneration, Diabetic or Hypertensive Retinopathy, Cataracts and many other diseases.

During your complete ocular visual assessment you will be screened for all conditions that may be affecting you as well as treat any issues you may be suffering from. Common treatable complaints: Dry eyes, Watery eyes, Burning, Itching, Difficulty reading small print, Reduced distance vision, Glare, Light sensitiveness, and difficulty performing hobbies.

Here is what your complete examination includes

Step 1: Appointment Request
-Call
-Email
-Phone
-Fax

Step 2: Welcome form
-Patient Name, DOB, QR Wellcover number
-List current medications, allergies
-Current Visual difficulties
-Previous spectacle prescription (if available)

Step 3: Ocular Visual Assessment and Discussion of Results
-History & Symptoms
-Refraction
-Dilation and thorough ocular/retinal screening
-Spectacle or magnifier dispense if required
-Ophthalmologist or medical practitioner referral if required

Step 4: Dispense and Delivery
-Return to fit custom made glasses
-Demonstrate use low vision device
-Discuss any questions/treatments/referrals

I have just increased the budget. I am running out of time and want some good designs. I want a modern, clean and clear product. Please submit, points for originality.

Target Market(s)

The target audience is Professionals, managers, senior care facilities, families. I want something clean and easy to read. I want something modern but not trendy and something that appeals to the masses.

Industry/Entity Type

Medical

Font styles to use
Sans Serif

Requirements
Must have
• easy to read
bright
professional
Contact information on the last page
Nice to have
• order of services layer out nicely. Try a version with clearly defined steps. Step 1. Step 2. Step 3. Could be multiple broachers that are packaged together.
Should not have
• cartoony
serif fonts (please use font that is in logo)

```html
<!DOCTYPE html>
<html lang="en">
<head>
<meta charset="utf-8">
<title>Mobile Optometry – Examination Steps</title>
<link href="https://fonts.googleapis.com/css2?family=Open+Sans:ital,wght@0,300;0,400;0,700;1,300&display=swap" rel="stylesheet">
<style>
  :root {
    --blue: #1b93cc;
    --blue-light: #5fb3df;
    --blue-pale: #a9cfe8;
    --gray-band: #a3aab1;
    --gray-panel: #efefef;
    --green: #0fa98c;
    --text-dark: #2f3033;
    --bullet: #1c8fcf;
    --white: #ffffff;
  }
  * { box-sizing: border-box; margin: 0; padding: 0; }
  html, body { width: 1200px; height: 934px; overflow: hidden; background: var(--white); }
  body { position: relative; font-family: "Open Sans", Arial, sans-serif; }

  .cover { position: absolute; left: 0; top: 0; width: 390px; height: 934px; background: var(--blue); }
  .cover-top {
    position: absolute; left: 0; top: 0; width: 390px; height: 244px;
    background: linear-gradient(180deg, #9fcbe6 0%, #4ea6d6 55%, #1b8fc8 100%);
  }
  .cover-quote {
    position: absolute; left: 40px; top: 58px; width: 310px; text-align: center;
    color: var(--white); font-weight: 300; font-style: italic; font-size: 28px; line-height: 38px;
  }
  .cover-quote .mark { font-style: normal; font-weight: 400; font-size: 34px; vertical-align: -4px; }
  .cover-photo {
    position: absolute; left: 0; top: 244px; width: 390px; height: 380px;
    background: linear-gradient(160deg, #e6edf4 0%, #c9d8e6 55%, #9fb6cb 100%);
  }

  .column { position: absolute; top: 0; height: 934px; }
  .column-mid { left: 432px; width: 348px; background: var(--gray-panel); top: 14px; height: 920px; }
  .column-right {
    left: 822px; width: 378px; top: 14px; height: 920px;
    background: linear-gradient(160deg, #f7efe9 0%, #efe6e1 45%, #e9ecef 100%);
  }

  .step-band { position: absolute; left: 0; width: 100%; height: 105px; }
  .band-gray { background: var(--gray-band); }
  .band-blue { background: var(--blue-pale); }
  .band-green { background: var(--green); }
  .step-label {
    position: absolute; left: 18px; top: 46px; color: var(--white);
    font-weight: 300; font-size: 33px; line-height: 40px;
  }
  .step-num {
    position: absolute; left: 90px; top: 52px; color: var(--white);
    font-weight: 700; font-size: 66px; line-height: 70px;
    text-shadow: 0 2px 3px rgba(0,0,0,0.12);
  }
  .step-rule { position: absolute; left: 148px; top: 76px; width: 120px; height: 1px; background: var(--white); }

  .step-title {
    position: absolute; left: 18px; color: var(--text-dark);
    font-weight: 400; font-size: 34px; line-height: 38px;
  }
  .step-list {
    position: absolute; left: 18px; list-style: none;
    color: var(--bullet); font-weight: 700; font-size: 16px; line-height: 19.5px;
  }
  .step-list li { position: relative; padding-left: 28px; }
  .step-list li::before { content: "•"; position: absolute; left: 0; top: 0; }
  .list-two-col { display: grid; grid-template-columns: 126px 150px; }

  .step-photo {
    position: absolute; left: 0; top: 270px; width: 348px; height: 194px;
    background: linear-gradient(90deg, #f1e4da 0%, #d9cfc9 50%, #3f4650 80%, #22262c 100%);
  }
</style>
</head>
<body>

<section class="cover">
  <div class="cover-top"></div>
  <p class="cover-quote"><span class="mark">“</span> Here is what your complete examination includes <span class="mark">”</span></p>
  <div class="cover-photo" role="img" aria-label="Photo of a hand holding eyeglasses in front of an eye chart"></div>
</section>

<section class="column column-mid">
  <div class="step-band band-gray" style="top:0">
    <span class="step-label">Step</span><span class="step-num">1</span><span class="step-rule"></span>
  </div>
  <h2 class="step-title" style="top:124px">Appointment<br>Request</h2>
  <ul class="step-list list-two-col" style="top:220px">
    <li>Call</li><li>Phone</li>
    <li>Email</li><li>Fax</li>
  </ul>
  <div class="step-photo" role="img" aria-label="Photo of a patient looking into an eye examination instrument"></div>

  <div class="step-band band-gray" style="top:504px">
    <span class="step-label">Step</span><span class="step-num">2</span><span class="step-rule"></span>
  </div>
  <h2 class="step-title" style="top:626px">Welcome<br>Form</h2>
  <ul class="step-list" style="top:720px">
    <li>Patient Name, DOB, QR<br>Wellcover number</li>
    <li>List current medications,<br>allergies</li>
    <li>Current Visual Difficulties</li>
    <li>Previous Spectacle<br>prescription (if available)</li>
  </ul>
</section>

<section class="column column-right" role="img" aria-label="Soft close-up photo of an eye as background">
  <div class="step-band band-blue" style="top:0">
    <span class="step-label">Step</span><span class="step-num">4</span><span class="step-rule"></span>
  </div>
  <h2 class="step-title" style="top:124px">Ocular Visual<br>Assessment and<br>Discussion<br>of Results</h2>
  <ul class="step-list" style="top:296px">
    <li>History &amp; Symptoms</li>
    <li>Refraction</li>
    <li>Dilation and thorough<br>ocular/retinal screening</li>
    <li>Spectacle or magnifier<br>dispense if required</li>
    <li>Ophthalmologist or<br>medical practitioner<br>referral if required</li>
  </ul>

  <div class="step-band band-green" style="top:504px">
    <span class="step-label">Step</span><span class="step-num">3</span><span class="step-rule"></span>
  </div>
  <h2 class="step-title" style="top:626px">Dispense and<br>Delivery</h2>
  <ul class="step-list" style="top:738px">
    <li>Return to fit custom<br>made glasses</li>
    <li>Demonstrate use low<br>vision device</li>
    <li>Discuss any questions/<br>treatments/referrals</li>
  </ul>
</section>

</body>
</html>
```